Corvane Project Services - Flyer

Project Breif:
I need a single page A4 Capability Statement, which will be used to market our services to prospective clients, both in print and via email PDF.
It needs to look professional and should incorporate the elements I have uploaded into files, these include:
Capability Statement Text
Corvane Services Company Logo
Additional Logo’s (Tools We Use)
Glimmer Bay Pics can be cut into the page
I have included examples of capability statements as a guide to what i am looking for.
Regards
Derek
Engineering Consulting

```html
<!DOCTYPE html>
<html lang="en">
<head>
<meta charset="utf-8">
<title>Corvane Project Services – Capability Statement</title>
<link href="https://fonts.googleapis.com/css2?family=Bowlby+One&family=Mulish:wght@400;600;700;800&display=swap" rel="stylesheet">
<style>
  :root {
    --navy: #0b3f8f;
    --blue: #0d4fa8;
    --deep: #0a3579;
    --ink: #333740;
    --grey: #8a9099;
    --silver: #b9bec5;
    --page-top: #ffffff;
    --page-bottom: #e9edf2;
    --footer: #0d4597;
    --white: #ffffff;
  }
  * { box-sizing: border-box; margin: 0; padding: 0; }
  html, body { width: 849px; height: 1200px; overflow: hidden; background: var(--white); }
  .flyer {
    position: relative;
    width: 849px;
    height: 1200px;
    overflow: hidden;
    font-family: "Mulish", sans-serif;
    color: var(--ink);
    background: linear-gradient(180deg, var(--page-top) 40%, var(--page-bottom) 100%);
  }
  .hero { position: absolute; left: 0; top: 0; width: 849px; height: 500px; }
  .brand {
    position: absolute; left: 36px; top: 30px; width: 190px;
    display: flex; flex-direction: column; align-items: center; gap: 8px;
    color: var(--deep); font-weight: 700; text-align: center;
  }
  .brand-dot { width: 56px; height: 56px; border-radius: 50%; background: var(--silver); }
  .brand-name { font-size: 15px; letter-spacing: 0.5px; line-height: 1.15; }
  .brand-name span { display: block; font-size: 11px; letter-spacing: 5px; }

  .inset-photo {
    position: absolute; left: 616px; top: 238px; width: 252px; height: 252px;
    border-radius: 50%; border: 9px solid var(--white);
    background: radial-gradient(circle at 55% 45%, #f4f6f9 0%, #d8dee6 55%, #b5c2cf 100%);
    box-shadow: 0 2px 6px rgba(0,0,0,.12);
  }

  .col-left { position: absolute; left: 36px; top: 486px; width: 400px; }
  .col-right { position: absolute; left: 476px; top: 502px; width: 340px; }
  .section-title {
    font-family: "Bowlby One", sans-serif; font-weight: 400;
    color: var(--blue); font-size: 24px; line-height: 1.2; margin-bottom: 4px;
  }
  .col-left .section-title { margin-top: 14px; }
  .col-left .section-title:first-child { margin-top: 0; }
  .col-left p { font-size: 15.2px; line-height: 21.7px; }
  .services-title { font-size: 25px; margin-bottom: 6px; }
  .service-group { color: var(--blue); font-weight: 700; font-size: 15.2px; line-height: 24px; }
  .service-list { list-style: none; }
  .service-list li {
    position: relative; padding-left: 22px; font-size: 15.2px; line-height: 19.5px; margin-bottom: 4.5px;
  }
  .service-list li::before {
    content: "✓"; position: absolute; left: 0; top: 0; color: var(--ink); font-size: 13px;
  }

  .tools-bar {
    position: absolute; left: 0; top: 1080px; width: 849px; height: 56px;
    background: var(--white);
    display: flex; align-items: center; justify-content: space-around; padding: 0 30px;
  }
  .tool { font-weight: 800; font-size: 14px; color: var(--grey); display: flex; align-items: center; gap: 6px; }
  .tool-mark { width: 12px; height: 12px; background: var(--silver); }

  .contact-bar {
    position: absolute; left: 0; top: 1136px; width: 849px; height: 64px;
    background: var(--footer); color: var(--white);
    display: flex; align-items: center; justify-content: center; gap: 14px;
    font-size: 19px; letter-spacing: 0.6px;
  }
  .contact-bar .label { color: #6f8fc4; font-weight: 400; }
  .contact-bar .sep { color: #5d7fb9; }
  .contact-bar b { font-weight: 700; }
</style>
</head>
<body>
<div class="flyer">
  <svg class="hero" viewBox="0 0 849 500" xmlns="http://www.w3.org/2000/svg">
    <defs>
      <linearGradient id="officeTone" x1="0" y1="0" x2="1" y2="1">
        <stop offset="0" stop-color="#e6eef7"/>
        <stop offset="0.5" stop-color="#c9d7e7"/>
        <stop offset="1" stop-color="#9fb4cc"/>
      </linearGradient>
      <linearGradient id="steel" x1="0" y1="0" x2="1" y2="0">
        <stop offset="0" stop-color="#d9dde2"/>
        <stop offset="0.5" stop-color="#9aa2ab"/>
        <stop offset="1" stop-color="#5e6670"/>
      </linearGradient>
    </defs>
    <path role="img" aria-label="Photograph of a bright meeting room with chairs, a table and a flip chart"
          d="M0 0 H849 V440 H0 Z" fill="url(#officeTone)"/>
    <path d="M790 0 H849 V260 C830 240 815 235 790 250 Z" fill="var(--deep)"/>
    <path d="M0 310 C60 360 140 380 230 360 C330 340 420 350 520 390 C600 420 680 450 760 440 V500 H0 Z" fill="var(--deep)"/>
    <path d="M0 410 C120 360 260 320 420 330 C540 338 620 400 700 430 C660 445 600 452 540 440 C440 420 330 380 220 385 C130 390 60 410 0 430 Z" fill="url(#steel)"/>
    <path d="M0 430 C90 410 170 395 260 395 C380 398 480 450 600 470 C680 480 760 470 849 455 V500 H0 Z" fill="var(--page-top)"/>
    <path d="M0 432 C110 405 220 392 320 400 C430 410 520 455 640 470" fill="none" stroke="var(--blue)" stroke-width="3"/>
  </svg>

  <div class="brand">
    <div class="brand-dot"></div>
    <div class="brand-name">CORVANE PROJECT<span>SERVICES</span></div>
  </div>

  <div class="inset-photo" role="img" aria-label="Photograph of hands reviewing printed charts and reports"></div>

  <section class="col-left">
    <h2 class="section-title">ABOUT US:</h2>
    <p>Our goal is to make successful project delivery more achievable and repeatable. We are continually innovating, evolving and learning, utilizing the latest industry tools and techniques to deliver real value to our clients. We are passionate about empowering organisations to achieve their objectives, on time and on budget.</p>
    <h2 class="section-title">Our Team</h2>
    <p>We use highly experienced industry professionals who engage with our clients to deliver practical and innovative project control solutions.</p>
    <h2 class="section-title">Our Expertise</h2>
    <p>For over 20 years we have been helping our clients to successfully deliver capital projects within the pharmaceutical and biotechnology sectors. During this time, we have worked closely with multinational healthcare companies and leading A&amp;E firms, on a variety of business-critical projects. Our experience and knowledge of project control gives our client’s unparalleled visibility of Cost, Schedule and Risk through the life cycle of their projects. This visibility allows our clients to make timely informed decisions which increase efficiency and project performance.</p>
  </section>

  <section class="col-right">
    <h2 class="section-title services-title">Core Services:</h2>
    <h3 class="service-group">Planning and Scheduling</h3>
    <ul class="service-list">
      <li>Tender Planning</li>
      <li>Interactive Planning / Pull Planning</li>
      <li>CPM Planning &amp; Scheduling</li>
      <li>Agile / Lean Planning Methodology</li>
      <li>Independent Schedule Quality Assessment</li>
      <li>Schedule Risk Analysis (Monte Carlo)</li>
      <li>Training</li>
    </ul>
    <h3 class="service-group">Management of Risk</h3>
    <ul class="service-list">
      <li>Risk Management Policies &amp; Procedures</li>
      <li>Risk Management Strategy</li>
      <li>Risk Registers</li>
      <li>Risk Response and Communication</li>
      <li>Cost &amp; Schedule Risk Analysis (Monte Carlo)</li>
      <li>Risk Management Training</li>
    </ul>
    <h3 class="service-group">Cost Control:</h3>
    <ul class="service-list">
      <li>Estimating &amp; Forecasting</li>
      <li>Earned Value Management</li>
      <li>Progress Reporting</li>
      <li>Cost Risk Analysis (Monte Carlo)</li>
    </ul>
  </section>

  <div class="tools-bar">
    <span class="tool">Tessera Planner</span>
    <span class="tool"><span class="tool-mark"></span>Plotline</span>
    <span class="tool">Arbor Schedule</span>
    <span class="tool">Waymark Pro</span>
    <span class="tool">Keystone Gauge</span>
    <span class="tool">RiskWell</span>
  </div>

  <footer class="contact-bar">
    <span><span class="label">e:</span> info@<b>corvaneservices</b>.ie</span>
    <span class="sep">|</span>
    <span><span class="label">w:</span> www.<b>corvaneservices</b>.ie</span>
    <span class="sep">|</span>
    <span><span class="label">p:</span> <b>+353 (0)870 555 0148</b></span>
  </footer>
</div>
</body>
</html>
```